Amber Meadow Method at The Pilates Harbor

I am looking for a poster that I can hang (long term) in a hospital or other clinic (cancer clinic, physiotherapy clinic). The poster should convey that Pilates is the best way to get back into movement after surgery/radiation/chemotherapy. Pilates will keep you moving efficiently, prevent imbalances, improve blood flow to name a few. My website is thepilatesharbor.example for details of my studio and the website to look at for further details on the program and full list of benefits is ambermeadowmethod.example.

Target Market(s)

Breast cancer survivors

Industry/Entity Type

Clinic

Requirements
Must have
• Must convey my program training/certification, my high quality of teaching, clients are in a safe, supportive place.
• My studio address, my name.
Nice to have
• We offer this work in both a group setting or privately (one to one).

```html
<!DOCTYPE html>
<html lang="en">
<head>
<meta charset="utf-8">
<title>Amber Meadow Method at The Pilates Harbor</title>
<link href="https://fonts.googleapis.com/css2?family=Oswald:wght@400;600&family=Quicksand:wght@700&family=Open+Sans:ital,wght@1,700&display=swap" rel="stylesheet">
<style>
  :root {
    --green: #7cbb2e;
    --green-dark: #4f8a1c;
    --green-light: #b6dc74;
    --grey-text: #6b6b6b;
    --grey-head: #5e6a6a;
    --white: #ffffff;
  }
  * { box-sizing: border-box; margin: 0; padding: 0; }
  html, body { width: 768px; height: 1200px; overflow: hidden; background: var(--white); }
  .poster { position: relative; width: 768px; height: 1200px; overflow: hidden; background: var(--white); font-family: "Quicksand", sans-serif; }

  .hero-photo {
    position: absolute; left: 0; top: 0; width: 768px; height: 600px;
    background:
      radial-gradient(ellipse 260px 200px at 140px 280px, rgba(40,40,40,0.55), transparent 70%),
      radial-gradient(ellipse 160px 140px at 330px 330px, rgba(50,90,170,0.45), transparent 70%),
      radial-gradient(ellipse 140px 120px at 470px 360px, rgba(30,30,30,0.45), transparent 70%),
      radial-gradient(ellipse 110px 100px at 560px 380px, rgba(200,60,110,0.35), transparent 70%),
      linear-gradient(180deg, #eef0ec 0%, #dfe2dc 40%, #b4a58c 75%, #8d7c62 100%);
  }
  .swoosh { position: absolute; left: 0; top: 460px; width: 768px; height: 180px; }

  .brand {
    position: absolute; display: flex; align-items: center; gap: 8px;
    font-weight: 700; font-size: 15px; color: var(--green-dark);
  }
  .brand-studio { left: 150px; top: 18px; }
  .brand-program { left: 470px; top: 18px; color: #c2456e; }
  .brand-mark-circle { width: 18px; height: 18px; border-radius: 50%; background: var(--green); }
  .brand-mark-square { width: 16px; height: 16px; background: #e58aa8; }

  .price { position: absolute; right: 22px; top: 100px; text-align: right; color: var(--green); font-family: "Oswald", sans-serif; }
  .price-label { font-weight: 600; font-size: 30px; letter-spacing: 1px; line-height: 1; }
  .price-amount { font-weight: 400; font-size: 112px; line-height: 1; }

  .headline {
    position: absolute; right: 20px; top: 624px; text-align: center;
    font-weight: 700; font-size: 50px; line-height: 1.12;
  }
  .headline-lead { display: block; color: var(--green); margin-right: 30px; }
  .headline-tail { display: block; color: var(--grey-head); }

  .details {
    position: absolute; right: 22px; top: 748px; width: 730px; text-align: right;
    font-family: "Open Sans", sans-serif; font-style: italic; font-weight: 700;
    font-size: 13.5px; line-height: 1.6; color: var(--grey-text);
  }
  .details-note { color: var(--green); }

  .studio-photo {
    position: absolute; left: 0; top: 880px; width: 768px; height: 320px;
    background:
      radial-gradient(ellipse 120px 140px at 420px 70px, rgba(150,190,120,0.7), transparent 70%),
      radial-gradient(ellipse 90px 140px at 110px 180px, rgba(30,30,30,0.45), transparent 70%),
      radial-gradient(ellipse 80px 130px at 300px 190px, rgba(210,70,90,0.35), transparent 70%),
      radial-gradient(ellipse 80px 130px at 470px 190px, rgba(50,90,170,0.35), transparent 70%),
      radial-gradient(ellipse 80px 130px at 640px 180px, rgba(30,30,30,0.4), transparent 70%),
      linear-gradient(180deg, #e6e2da 0%, #b9ab95 55%, #7d6b55 100%);
  }

  .contact-panel {
    position: absolute; left: 166px; top: 1036px; width: 424px; height: 154px;
    background: rgba(124, 187, 46, 0.82); color: var(--white);
  }
  .pin-frame {
    position: absolute; left: 14px; top: 18px; width: 58px; height: 58px;
    border: 3px solid var(--white); display: flex; align-items: center; justify-content: center;
  }
  .address { position: absolute; left: 90px; top: 14px; font-weight: 700; font-size: 26px; line-height: 1.2; }
  .owner-name {
    position: absolute; left: 0; bottom: 12px; width: 100%; text-align: center;
    font-weight: 700; font-size: 25px; letter-spacing: 1px; text-transform: uppercase;
  }
  .brand-footer { left: 610px; top: 1150px; color: var(--white); font-size: 16px; }
</style>
</head>
<body>
<main class="poster">
  <div class="hero-photo" role="img" aria-label="Women exercising together on Pilates reformer machines in a bright studio"></div>

  <svg class="swoosh" viewBox="0 0 768 180" preserveAspectRatio="none" aria-hidden="true">
    <path d="M0 110 C 240 60, 520 20, 768 0 L 768 30 C 520 50, 260 90, 0 140 Z" fill="var(--green-light)"/>
    <path d="M0 135 C 250 85, 520 45, 768 25 L 768 180 L 0 180 Z" fill="var(--green)"/>
    <path d="M0 165 C 260 115, 530 80, 768 60 L 768 180 L 0 180 Z" fill="var(--white)"/>
  </svg>

  <div class="brand brand-studio"><span class="brand-mark-circle"></span>The Pilates Harbor</div>
  <div class="brand brand-program"><span class="brand-mark-square"></span>Amber Meadow Method</div>

  <div class="price">
    <div class="price-label">STARTING FROM</div>
    <div class="price-amount">$18</div>
  </div>

  <h1 class="headline">
    <span class="headline-lead">Get Back To Living</span>
    <span class="headline-tail">No Just Surviving</span>
  </h1>

  <p class="details">
    We strongly urge that every client starts with a private session to maximize their experience.<br>
    To get the most out of starting a Pilates program, commit to a mat and an apparatus class per week.<br>
    We offer 10% off for seniors (65+) and students (with valid ID) excluding New Client pkg.<br>
    <span class="details-note">*Work is offered in both a group setting or privately</span>
  </p>

  <div class="studio-photo" role="img" aria-label="Instructor and clients standing on reformers with arms outstretched in the studio"></div>

  <section class="contact-panel">
    <div class="pin-frame">
      <svg width="28" height="36" viewBox="0 0 26 34" aria-hidden="true">
        <path d="M13 1 C6 1 1 6 1 13 C1 22 13 33 13 33 C13 33 25 22 25 13 C25 6 20 1 13 1 Z" fill="var(--white)"/>
        <circle cx="13" cy="13" r="5" fill="var(--green)"/>
      </svg>
    </div>
    <div class="address">#204-118 Harbourview Rd.<br>Riverton, B.C., Canada</div>
    <div class="owner-name">Claire Whitford</div>
  </section>

  <div class="brand brand-footer">The Pilates Harbor</div>
</main>
</body>
</html>
```